Equestrian industry - Problem solving and creative skills required!

I have just joined a saddle fitting franchise that has an existing logo that I would like to tweak (see Summit Tackworks file for the original logo). The franchise doesn't have any real colour scheme except that the horse logo (attached - logoonly) must stay orange and the words 'Summit Tackworks' must stay white. Apart from that I have free reign to use what ever colours etc I like. I have chosen some colours that I would like to work with (see chosen colours file). I don't want anything drastically different because I still have to represent myself as part of the franchise, however I would like to make it more modern and make it my own.

My business name is 'Summit Tackworks Western Australia' but the Western Australia can be shortened to 'WA'. My business is about integrity, expert knowledge and empathy.

Could you please play with the chosen colours and the existing logo to create a logo that is less 80's and more in this decade. I would also like you to create a stationary package including a form header, letterhead and business card etc.

I am also able to provide the logo in vector format if required.

Thank you!

Target Market(s)

Grass Roots horse riders - usually middle aged women

Industry/Entity Type

Industry

Contact Information for Business Card

Dana Whitcombe
Phone: 0417385926
email:dana@summittackworks.net.au
Facebook page and web address to come

Logo Text

Summit Tackworks Western Australia

Logo styles of interest
Emblem Logo
Pictorial/Combination Logo
Abstract Logo
Requirements
Must have
• Existing jumping horse image incorporated.
• Colour of horse logo to stay the same.
• Prefer to keep the words 'Summit Tackworks' white.
Nice to have
• more modern
• using chosen colours
Should not have
• changed the existing jumping horse image
• be too far removed from the original logo

```html
<!DOCTYPE html>
<html lang="en">
<head>
<meta charset="utf-8">
<title>Summit Tackworks Western Australia – Stationery</title>
<link href="https://fonts.googleapis.com/css2?family=Questrial&display=swap" rel="stylesheet">
<style>
  :root {
    --teal: #10546f;
    --orange: #e2622b;
    --paper: #f5f5f4;
    --ink: #4a4a4a;
    --backdrop: #d6d6d6;
  }
  * { margin: 0; padding: 0; box-sizing: border-box; }
  html, body { width: 1200px; height: 900px; overflow: hidden; }
  body {
    background: var(--backdrop);
    font-family: "Questrial", sans-serif;
    color: var(--ink);
    position: relative;
  }
  .sheet { position: absolute; background: var(--paper); overflow: hidden; }
  .sheet--dark { background: var(--teal); }

  .brand { position: absolute; display: flex; align-items: center; gap: 0.35em; }
  .brand-dot { width: 0.9em; height: 0.9em; border-radius: 50%; background: var(--orange); flex: none; }
  .brand-name { font-weight: 400; line-height: 1.05; color: var(--teal); }
  .brand-name small { display: block; font-size: 0.42em; letter-spacing: 0.08em; text-transform: uppercase; margin-top: 0.2em; }
  .brand--light .brand-name { color: #fff; }

  .contact { position: absolute; line-height: 1.45; color: var(--ink); }
  .contact li { list-style: none; display: flex; align-items: center; gap: 0.5em; }
  .contact .icon { width: 0.95em; height: 0.95em; background: var(--orange); border-radius: 1px; flex: none; }
  .contact .address { margin-top: 0.9em; }

  .wave { position: absolute; left: 0; bottom: 0; width: 100%; display: block; }

  /* letterhead */
  .letterhead { left: 220px; top: 54px; width: 382px; height: 540px; }
  .letterhead .brand { left: 40px; top: 36px; font-size: 12px; }
  .letterhead .contact { left: 282px; top: 38px; font-size: 5.6px; }

  /* folder */
  .folder { left: 650px; top: 40px; width: 415px; height: 553px; border-radius: 3px; }
  .folder-spine { position: absolute; left: 0; top: 0; width: 22px; height: 100%; background: rgba(0,0,0,0.08); border-right: 1px solid rgba(255,255,255,0.06); }
  .folder .brand { left: 166px; top: 92px; font-size: 19px; }

  /* business cards */
  .card { width: 163px; height: 91px; left: 79px; }
  .card--front { top: 638px; }
  .card--back { top: 748px; }
  .card--front .brand { left: 14px; top: 34px; font-size: 6.4px; }
  .card-person { position: absolute; left: 100px; top: 19px; font-size: 4.6px; }
  .card-person .name { color: var(--orange); font-size: 5.4px; letter-spacing: 0.04em; text-transform: uppercase; }
  .card-person .role { margin-bottom: 3px; }
  .card--front .contact { position: static; font-size: 4.2px; }
  .card--back .brand { left: 62px; top: 40px; font-size: 8.6px; }

  /* compliment slip */
  .slip { left: 278px; top: 640px; width: 400px; height: 199px; }
  .slip .brand { left: 20px; top: 26px; font-size: 10.5px; }
  .slip .address { position: absolute; left: 38px; top: 70px; font-size: 5px; line-height: 1.4; }

  /* envelope */
  .envelope { left: 724px; top: 640px; width: 400px; height: 199px; }
  .envelope-flap { position: absolute; left: 0; top: 0; width: 100%; height: 57px; display: block; }
  .envelope-mark { position: absolute; left: 191px; top: 22px; width: 12px; height: 12px; border-radius: 50%; background: var(--orange); }
</style>
</head>
<body>

  <section class="sheet letterhead" aria-label="Letterhead">
    <div class="brand">
      <span class="brand-dot"></span>
      <span class="brand-name">Summit Tackworks<small>Western Australia</small></span>
    </div>
    <ul class="contact">
      <li><span class="icon"></span>08-9321-4780</li>
      <li><span class="icon"></span>08-9321-4781</li>
      <li><span class="icon"></span>hello@summittackworks.net.au</li>
      <li><span class="icon"></span>www.summittackworks.net.au</li>
      <li class="address">14 Paddock Ridge Road<br>Bunbury, WA 6230</li>
    </ul>
    <svg class="wave" viewBox="0 0 382 30" preserveAspectRatio="none" height="30">
      <path d="M0,12 C110,8 250,-2 382,2 L382,8 C270,8 150,18 40,30 L0,30 Z" fill="var(--orange)"/>
      <path d="M110,30 C200,18 300,10 382,10 L382,30 Z" fill="var(--teal)" stroke="#fff" stroke-width="1.5"/>
    </svg>
  </section>

  <section class="sheet sheet--dark folder" aria-label="Presentation folder">
    <div class="folder-spine"></div>
    <div class="brand brand--light">
      <span class="brand-dot"></span>
      <span class="brand-name">Summit Tackworks<small>Western Australia</small></span>
    </div>
  </section>

  <section class="sheet card card--front" aria-label="Business card front">
    <div class="brand">
      <span class="brand-dot"></span>
      <span class="brand-name">Summit Tackworks<small>Western Australia</small></span>
    </div>
    <div class="card-person">
      <p class="name">Dana Whitcombe</p>
      <p class="role">General Manager</p>
      <ul class="contact">
        <li><span class="icon"></span>0417385926</li>
        <li><span class="icon"></span>08-9321-4781</li>
        <li><span class="icon"></span>dana@summittackworks.net.au</li>
        <li><span class="icon"></span>www.summittackworks.net.au</li>
        <li class="address">14 Paddock Ridge Road<br>Bunbury, WA 6230</li>
      </ul>
    </div>
    <svg class="wave" viewBox="0 0 163 10" preserveAspectRatio="none" height="10">
      <path d="M0,5 C50,3 110,0 163,1 L163,3 C110,3 60,6 15,10 L0,10 Z" fill="var(--orange)"/>
      <path d="M45,10 C85,5 130,3 163,3.5 L163,10 Z" fill="var(--teal)" stroke="#fff" stroke-width="0.6"/>
    </svg>
  </section>

  <section class="sheet sheet--dark card card--back" aria-label="Business card back">
    <div class="brand brand--light">
      <span class="brand-dot"></span>
      <span class="brand-name">Summit Tackworks<small>Western Australia</small></span>
    </div>
  </section>

  <section class="sheet slip" aria-label="Compliment slip">
    <div class="brand">
      <span class="brand-dot"></span>
      <span class="brand-name">Summit Tackworks<small>Western Australia</small></span>
    </div>
    <p class="address">14 Paddock Ridge Road<br>Bunbury, WA 6230</p>
    <svg class="wave" viewBox="0 0 400 26" preserveAspectRatio="none" height="26">
      <path d="M0,12 C120,8 260,-1 400,2 L400,7 C280,7 160,16 40,26 L0,26 Z" fill="var(--orange)"/>
      <path d="M120,26 C210,15 310,9 400,9 L400,26 Z" fill="var(--teal)" stroke="#fff" stroke-width="1.4"/>
    </svg>
  </section>

  <section class="sheet envelope" aria-label="Envelope">
    <svg class="envelope-flap" viewBox="0 0 400 57" preserveAspectRatio="none">
      <path d="M0,0 L400,0 L385,57 L15,57 Z" fill="var(--teal)"/>
    </svg>
    <span class="envelope-mark"></span>
  </section>

</body>
</html>
```